Northfield Builders Guild Business card

We are looking for a new business card design with photo included.
Our business is a nonprofit construction contractor membership organization. We offer business education, assist with business setup and licensing, provide safety training, and provide a member directory.
URL: www.brickwayguildnetwork.org
Color code:
CMYK: 0 cyan, 42 magenta, 100 yellow, 0 black for Print.
Hexidecimal: #FF9900
RGB: R 255; G 153; B 0

```html
<!DOCTYPE html>
<html lang="en">
<head>
<meta charset="utf-8">
<title>Northfield Builders Guild – Business Card</title>
<link rel="stylesheet" href="https://fonts.googleapis.com/css2?family=Arimo:wght@400;700&display=swap">
<style>
  :root {
    --brand-orange: #FF9900;
    --card-orange: #F6A321;
    --ink: #111111;
    --text-grey: #666666;
    --rule-grey: #8a8a8a;
    --paper: #FFFFFF;
    --backdrop: #E4E4E2;
  }
  * { margin: 0; padding: 0; box-sizing: border-box; }
  html, body {
    width: 1200px; height: 801px; overflow: hidden;
    background: var(--backdrop);
    font-family: "Arimo", Arial, sans-serif;
  }
  .stage {
    position: relative; width: 1200px; height: 801px;
    display: flex; align-items: center; justify-content: center; gap: 40px;
  }
  .card {
    position: relative; width: 540px; height: 309px; overflow: hidden;
    box-shadow: 0 6px 18px rgba(0,0,0,0.18);
  }
  .card--front { background: var(--paper); border-bottom: 3px solid var(--brand-orange); }
  .card--back { background: var(--card-orange); display: flex; align-items: center; justify-content: center; }

  .wordmark {
    font-weight: 700; color: var(--ink); text-transform: uppercase; letter-spacing: 0.02em;
  }
  .card--front .wordmark {
    position: absolute; top: 40px; left: 0; right: 0; text-align: center; font-size: 26px;
    white-space: nowrap;
  }
  .card--back .wordmark {
    width: 460px; text-align: center; font-size: 34px; line-height: 1.15;
  }

  .person { position: absolute; left: 36px; top: 118px; }
  .person__name { color: var(--brand-orange); font-weight: 700; font-size: 24px; }
  .person__title { color: var(--text-grey); font-size: 17px; margin-top: 4px; }

  .address {
    position: absolute; right: 36px; top: 126px; text-align: right; font-style: normal;
    color: var(--text-grey); font-size: 15px; line-height: 1.35;
  }
  .divider {
    position: absolute; left: 36px; right: 36px; top: 180px; height: 1px; background: var(--rule-grey);
  }
  .contacts { position: absolute; left: 36px; top: 196px; list-style: none; }
  .contacts__item {
    display: flex; align-items: center; gap: 10px;
    color: var(--text-grey); font-size: 15px; height: 27px;
  }
  .contacts__icon { width: 20px; height: 20px; flex: none; }
</style>
</head>
<body>
<main class="stage">
  <section class="card card--front" aria-label="Business card front">
    <div class="wordmark">Northfield Builders Guild</div>

    <div class="person">
      <div class="person__name">Dana Whitfield</div>
      <div class="person__title">Manager</div>
    </div>

    <address class="address">Your address, city<br>state, ZIP 0000</address>

    <div class="divider"></div>

    <ul class="contacts">
      <li class="contacts__item">
        <svg class="contacts__icon" viewBox="0 0 20 20" aria-hidden="true">
          <rect width="20" height="20" rx="4" fill="var(--brand-orange)"/>
          <path d="M6 4.5c1 0 1.6 2.4 1.2 3-.4.5-1 .7-.6 1.5.7 1.3 1.6 2.2 2.9 2.9.8.4 1-.2 1.5-.6.6-.4 3 .2 3 1.2 0 1.4-1.2 2.5-2.6 2.3C7.7 14.3 5.7 12.3 4.7 8.6 4.4 7 4.9 4.5 6 4.5z" fill="#fff"/>
        </svg>
        <span>555-014-2290</span>
      </li>
      <li class="contacts__item">
        <svg class="contacts__icon" viewBox="0 0 20 20" aria-hidden="true">
          <rect width="20" height="20" rx="4" fill="var(--brand-orange)"/>
          <rect x="4" y="6" width="12" height="8.5" fill="none" stroke="#fff" stroke-width="1.4"/>
          <path d="M4 6l6 5 6-5" fill="none" stroke="#fff" stroke-width="1.4"/>
        </svg>
        <span>dana@brickwayguildnetwork.org</span>
      </li>
      <li class="contacts__item">
        <svg class="contacts__icon" viewBox="0 0 20 20" aria-hidden="true">
          <rect width="20" height="20" rx="4" fill="var(--brand-orange)"/>
          <circle cx="10" cy="10" r="5.5" fill="none" stroke="#fff" stroke-width="1.3"/>
          <ellipse cx="10" cy="10" rx="2.4" ry="5.5" fill="none" stroke="#fff" stroke-width="1.1"/>
          <path d="M4.5 10h11" stroke="#fff" stroke-width="1.1"/>
        </svg>
        <span>www.brickwayguildnetwork.org</span>
      </li>
    </ul>
  </section>

  <section class="card card--back" aria-label="Business card back">
    <div class="wordmark">Northfield Builders<br>Guild</div>
  </section>
</main>
</body>
</html>
```